Landing Page - Mortgage Loan Intake

We are a mortgage company seeking a clean, easy-to-use landing page that consists of minimal copy and creative with a short intake form for customers to sign up to work with us on securing their home financing. We will soon have PX and Google campaigns running throughout the US, and those ads will lead to this landing page. We need at least one landing page for now and may need a slightly different version for A/B testing,. We will expand the project at the beginning of next year with additional versions with the same branding, just geared towards slightly different loan products.

This is the existing intake form we would incorporate on our landing page:

https://apply.quovafin.com/#/create-account

Here is some of the existing content that we would use as a springboard for the design, color scheme, and content of the landing page:

https://brindlehomeloans.com/https://brindlehomeloans.com/about/https://brindlehomeloans.com/refinance/consolidate-debt/

I have also included images that are related to what we're looking for either visually (feel and format) or in terms of the message.

Target Market(s)

people (borrowers) looking for a refinance or debt consolidation through a refinance

Industry/Entity Type

Mortgage Lender

Number of Pages Required

1 page

Font styles to use
Other font styles liked:
• unsure of the name but we would use the font currently used on brindlehomeloans.com

Colors
9bcb3b
cee9f5
ffffff
85acd3
cfeae6
abd036
cadf82
cedeed

Requirements
Must have
• intake form, clean light feel
Nice to have
• explanation of debt consolidation benefits or easy process via a simple infographic or illustration with a clean layout
Should not have
• anything off-brand (colors that are too heavy or not clean and airy)

```html
<!DOCTYPE html>
<html lang="en">
<head>
<meta charset="utf-8">
<title>Brindle Home Loans – Get your loan approved fast</title>
<link href="https://fonts.googleapis.com/css2?family=Lato:wght@300;400;700;900&family=Montserrat:wght@600;700&display=swap" rel="stylesheet">
<style>
:root{
  --green:#8cc232;
  --green-soft:#abd036;
  --green-pale:#cadf82;
  --blue:#7299cf;
  --blue-footer:#7197cf;
  --ink:#222;
  --muted:#666;
  --white:#fff;
  --gold:#f3a82a;
  --paper:#f1f1ef;
}
*{box-sizing:border-box;margin:0;padding:0}
html,body{width:1200px;height:3377px;overflow:hidden}
body{font-family:'Lato',sans-serif;color:var(--ink);background:var(--white);position:relative}
.abs{position:absolute}

/* hero */
.hero{position:absolute;left:0;top:0;width:1200px;height:712px;overflow:hidden}
.hero-photo{position:absolute;inset:0;background:linear-gradient(180deg,#2b2b2b 0%,#5a5956 35%,#9c9890 70%,#cfcac1 100%)}
.hero-shade{position:absolute;inset:0;background:linear-gradient(180deg,rgba(0,0,0,.45),rgba(0,0,0,.05) 60%)}
.nav{position:absolute;top:28px;left:0;width:1200px;height:40px}
.brand{position:absolute;left:168px;top:8px;display:flex;align-items:center;gap:8px;color:var(--white);font-weight:900;font-size:18px;white-space:nowrap}
.brand-mark{width:14px;height:14px;background:var(--white);border-radius:50%}
.nav-links{position:absolute;right:170px;top:9px;display:flex;gap:24px;list-style:none}
.nav-links li{color:var(--white);font-size:16.5px;white-space:nowrap}
.hero-title{position:absolute;top:210px;width:100%;text-align:center;font-family:'Montserrat',sans-serif;font-weight:700;font-size:45px;color:var(--white)}
.signup{position:absolute;left:272px;top:290px;width:680px;height:180px;background:var(--green);border-radius:3px}
.field{position:absolute;width:300px;height:48px;background:var(--white);border-radius:2px;display:flex;align-items:center;padding-left:16px;gap:10px;font-size:16px;color:#444}
.field svg{width:15px;height:15px}
.btn-create{position:absolute;left:349px;top:95px;width:300px;height:48px;background:#3b3d3f;color:var(--white);font-size:20px;display:flex;align-items:center;justify-content:center;border-radius:2px}
.hero-arrow{position:absolute;top:320px;width:34px;height:60px}

/* quick circles */
.quick{position:absolute;top:652px;width:226px;height:226px;border-radius:50%;text-align:center;box-shadow:0 4px 14px rgba(0,0,0,.18)}
.quick.light{background:var(--white);color:#333}
.quick.dark{background:var(--blue);color:var(--white)}
.quick svg.ic{margin-top:34px;width:70px;height:70px}
.quick p{font-size:16px;font-weight:700;letter-spacing:.5px;line-height:21px;margin-top:8px}
.quick .chev{position:absolute;left:96px;top:168px;width:34px;height:34px}

/* about */
.about{position:absolute;top:712px;left:0;width:1200px;height:677px;background:linear-gradient(180deg,#f6f6f4,#e9e8e4)}
.about-photo{position:absolute;left:0;top:230px;width:640px;height:447px;background:linear-gradient(135deg,#cfd8cf 0%,#b98a5a 45%,#ebe9e4 100%);opacity:.9}
.about h2{position:absolute;left:646px;top:278px;font-size:31px;font-weight:400;white-space:nowrap}
.about p{position:absolute;left:646px;top:326px;width:420px;font-size:13.5px;line-height:25px;color:#444}
.btn-learn{position:absolute;left:642px;top:477px;width:162px;height:40px;background:var(--green);color:var(--white);font-size:17px;display:flex;align-items:center;justify-content:center}

/* benefits */
.benefits{position:absolute;top:1389px;left:0;width:1200px;height:738px}
.section-title{position:absolute;width:100%;text-align:center;font-size:30px;font-weight:400}
.benefit h3{font-size:28px;font-weight:400;color:var(--green)}
.benefit p{font-size:15px;line-height:21px;color:#555;margin-top:4px}
.benefit{position:absolute}
.benefit.right{text-align:right}

/* testimonials */
.testimonials{position:absolute;top:2127px;left:0;width:1200px;height:442px;background:var(--green);overflow:hidden}
.testimonials .section-title{color:var(--white);top:48px}
.quote{position:absolute;text-align:center;border-radius:3px;overflow:hidden}
.quote.main{left:367px;top:119px;width:477px;height:228px;background:var(--white);box-shadow:0 4px 14px rgba(0,0,0,.2)}
.quote.side{top:140px;width:272px;height:180px;background:rgba(255,255,255,.18);color:rgba(255,255,255,.7)}
.qmark{font-family:Georgia,serif;font-size:60px;line-height:60px;color:var(--green);font-weight:700}
.quote.side .qmark{color:rgba(255,255,255,.55)}
.quote .text{font-size:18px;line-height:31px;color:#444;width:400px;margin:0 auto}
.quote.side .text{font-size:14px;line-height:24px;color:rgba(255,255,255,.8);white-space:nowrap}
.quote .name{font-size:18px;font-weight:700;margin-top:8px}
.stars{color:var(--gold);font-size:22px;letter-spacing:2px}
.t-arrow{position:absolute;top:213px;width:24px;height:40px}

/* news */
.news{position:absolute;top:2569px;left:0;width:1200px;height:637px}
.news h2{position:absolute;left:182px;top:74px;font-size:33px;font-weight:400}
.post-img{position:absolute;width:162px;height:162px;border-radius:50%}
.post{position:absolute;width:370px}
.post h3{font-size:19px;font-weight:700;line-height:26px}
.post p{font-size:14.5px;line-height:23px;color:#555;margin-top:12px}
.post a{display:block;margin-top:14px;color:var(--green);font-size:15px;text-decoration:none}
.ad{position:absolute;left:763px;width:259px}

/* footer */
.footer{position:absolute;top:3206px;left:0;width:1200px;height:171px;background:var(--blue-footer);text-align:center;color:var(--white)}
.footer ul{list-style:none;display:flex;justify-content:center;gap:30px;margin-top:34px;font-size:17px}
.footer small{display:block;font-size:12px;margin-top:10px}
.social{display:flex;justify-content:center;gap:6px;margin-top:18px}
.social span{width:34px;height:34px;border-radius:50%;background:var(--white)}
</style>
</head>
<body>

<header class="hero">
  <div class="hero-photo" role="img" aria-label="Bright modern living room with a sofa, cacti and hanging pendant lamps"></div>
  <div class="hero-shade"></div>
  <nav class="nav">
    <div class="brand"><span class="brand-mark"></span>Brindle Home Loans</div>
    <ul class="nav-links">
      <li>Refinance</li><li>Buy a House</li><li>Loan Options</li><li>Mortgage Rates</li><li>About</li><li>Loan Calculator</li>
    </ul>
  </nav>
  <h1 class="hero-title">Get your loan approved fast</h1>
  <form class="signup">
    <div class="field" style="left:39px;top:34px"><svg viewBox="0 0 16 16"><rect x="1" y="3" width="14" height="10" fill="none" stroke="#555" stroke-width="1.5"/><path d="M1 3l7 6 7-6" fill="none" stroke="#555" stroke-width="1.5"/></svg>Email address</div>
    <div class="field" style="left:349px;top:34px"><svg viewBox="0 0 16 16"><rect x="1" y="3" width="14" height="10" fill="none" stroke="#555" stroke-width="1.5"/><path d="M1 3l7 6 7-6" fill="none" stroke="#555" stroke-width="1.5"/></svg>Confirm Email address</div>
    <div class="field" style="left:39px;top:95px"><svg viewBox="0 0 16 16"><rect x="3" y="7" width="10" height="8" fill="none" stroke="#555" stroke-width="1.5"/><path d="M5 7V4a3 3 0 016 0v3" fill="none" stroke="#555" stroke-width="1.5"/></svg>Password</div>
    <div class="btn-create">Create Account</div>
  </form>
  <svg class="hero-arrow" style="left:100px" viewBox="0 0 34 60"><path d="M28 4L6 30l22 26" fill="none" stroke="#fff" stroke-width="4"/></svg>
  <svg class="hero-arrow" style="left:1066px" viewBox="0 0 34 60"><path d="M6 4l22 26-22 26" fill="none" stroke="#fff" stroke-width="4"/></svg>
</header>

<section class="about">
  <div class="about-photo" role="img" aria-label="Mint green armchair beside a wooden desk with a potted plant on a round rug"></div>
  <h2>About Brindle Home Loans</h2>
  <p>Integer congue augue et malesuada iaculis ipsum dui aliquet felis at cursus magna nisl nec elit Praesent elementum elit blandit sed nulla In ullamcorper est eget tempor cursus neque mi consectetuer mi a ultricies massa est sed nisl Class aptent taciti sociosqu ad litora torquent per conubia nostra per ince</p>
  <div class="btn-learn">Learn More</div>
</section>

<div class="quick light" style="left:189px">
  <svg class="ic" viewBox="0 0 70 70" fill="none" stroke="#8cc232" stroke-width="2.5"><path d="M22 58V40a16 16 0 1132 0v6l5 6h-5v6H38v-4"/><path d="M32 36l6-6 6 6v8H32z"/></svg>
  <p>HOME<br>BUYER TIPS</p>
  <svg class="chev" viewBox="0 0 34 34" fill="none" stroke="#555" stroke-width="1.5"><circle cx="17" cy="17" r="15"/><path d="M11 14l6 6 6-6"/></svg>
</div>
<div class="quick dark" style="left:382px">
  <svg class="ic" viewBox="0 0 70 70" fill="none" stroke="#fff" stroke-width="2.5"><path d="M35 12a16 16 0 00-9 29v7h18v-7a16 16 0 00-9-29z"/><path d="M28 54h14M30 60h10"/></svg>
  <p>REFINANCE<br>TIPS</p>
  <svg class="chev" viewBox="0 0 34 34" fill="none" stroke="#fff" stroke-width="1.5"><circle cx="17" cy="17" r="15"/><path d="M11 14l6 6 6-6"/></svg>
</div>
<div class="quick light" style="left:596px">
  <svg class="ic" viewBox="0 0 70 70" fill="none" stroke="#8cc232" stroke-width="2.5"><circle cx="24" cy="46" r="12"/><circle cx="46" cy="42" r="12"/><path d="M20 10v16M30 6v16M40 10v16M50 6v16"/></svg>
  <p>MORTGAGE<br>RATES</p>
  <svg class="chev" viewBox="0 0 34 34" fill="none" stroke="#555" stroke-width="1.5"><circle cx="17" cy="17" r="15"/><path d="M11 14l6 6 6-6"/></svg>
</div>
<div class="quick dark" style="left:787px">
  <svg class="ic" viewBox="0 0 70 70" fill="none" stroke="#fff" stroke-width="2.5"><rect x="16" y="14" width="34" height="46" rx="2"/><rect x="21" y="20" width="24" height="8"/><path d="M22 36h6M32 36h6M22 44h6M32 44h6M22 52h6M32 52h6"/><circle cx="50" cy="14" r="9"/></svg>
  <p>MORTGAGE<br>CALCULATOR</p>
  <svg class="chev" viewBox="0 0 34 34" fill="none" stroke="#fff" stroke-width="1.5"><circle cx="17" cy="17" r="15"/><path d="M11 14l6 6 6-6"/></svg>
</div>

<section class="benefits">
  <h2 class="section-title" style="top:56px">Our Benefits</h2>
  <svg class="abs" style="left:0;top:0" width="1200" height="738" viewBox="0 0 1200 738">
    <defs><radialGradient id="face" cx=".4" cy=".35"><stop offset="0" stop-color="#fff"/><stop offset="1" stop-color="#e6e6e6"/></radialGradient></defs>
    <path d="M770 290 Q730 300 690 300" stroke="#8cc232" stroke-width="26" fill="none"/>
    <path d="M585 478 Q540 490 500 490" stroke="#8cc232" stroke-width="26" fill="none"/>
    <circle cx="806" cy="202" r="92" fill="url(#face)" stroke="#8cc232" stroke-width="20"/>
    <circle cx="617" cy="385" r="92" fill="url(#face)" stroke="#7299cf" stroke-width="20"/>
    <circle cx="446" cy="578" r="92" fill="url(#face)" stroke="#8cc232" stroke-width="20"/>
    <g fill="none" stroke="#8cc232" stroke-width="3">
      <path d="M776 202l30-26 30 26v26h-60z"/><rect x="798" y="208" width="16" height="20"/>
      <path d="M766 236q20 10 40 6l30-10"/>
      <rect x="597" y="350" width="38" height="68" rx="4" stroke="#7299cf"/>
      <path d="M605 365h32v20h-20l-8 6v-6h-4z" stroke="#7299cf"/>
      <path d="M406 578l20-14 18 8 20-10 22 16M426 564l-10 22 30 14 14-12M446 572l12 14"/>
    </g>
  </svg>
  <div class="benefit right" style="left:295px;top:138px;width:380px">
    <h3>Priority</h3>
    <p>We will handle your home financing needs from here on out. Even after you close, we'll continue to find ways to improve your finances and reward you.</p>
  </div>
  <div class="benefit right" style="left:186px;top:330px;width:300px">
    <h3>Attention</h3>
    <p>We will return your calls by the end of the day. Your happiness is our #1 priority.</p>
  </div>
  <div class="benefit" style="left:570px;top:536px;width:300px">
    <h3>Promise</h3>
    <p>Something not right? Tell us and we'll do whatever we can to fix it.</p>
  </div>
</section>

<section class="testimonials">
  <h2 class="section-title">Testimonials</h2>
  <div class="quote side" style="left:-2px">
    <div class="qmark" style="margin-top:16px">“</div>
    <div class="text" style="margin-left:-90px">All electronic, very accommodadating<br>fast and can be done anywhere</div>
    <div class="name" style="font-size:15px;color:#3b5a12">By Author</div>
    <div class="stars" style="font-size:16px">★★★★★</div>
  </div>
  <div class="quote main">
    <div class="qmark" style="margin-top:18px">“</div>
    <div class="text">Super easy! All electronic, very accommodadating fast and can be done anywhere</div>
    <div class="name">Marlon T</div>
    <div class="stars">★★★★★</div>
  </div>
  <div class="quote side" style="left:939px">
    <div class="qmark" style="margin-top:16px">“</div>
    <div class="text" style="margin-left:30px;text-align:left">Super easy! All electronic, very acco<br>fast and can be done anywhere</div>
    <div class="name" style="font-size:15px;color:#3b5a12">By Author</div>
    <div class="stars" style="font-size:16px">★★★★★</div>
  </div>
  <svg class="t-arrow" style="left:306px" viewBox="0 0 24 40"><path d="M20 4L4 20l16 16" fill="none" stroke="#fff" stroke-width="4"/></svg>
  <svg class="t-arrow" style="left:870px" viewBox="0 0 24 40"><path d="M4 4l16 16L4 36" fill="none" stroke="#fff" stroke-width="4"/></svg>
</section>

<section class="news">
  <h2>News Blogs</h2>
  <div class="post-img" style="left:176px;top:141px;background:radial-gradient(circle at 40% 40%,#b9b4ab,#4a4640)" role="img" aria-label="Dining room interior with wooden table"></div>
  <div class="post" style="left:360px;top:156px">
    <h3>Integer congue malesuada</h3>
    <p>Aaculis ipsum dui aliquet felis at cursus magna nisl nec elit Praesent elementum elit at tellus nec ultricies sit amet porttitor mattis enim</p>
    <a href="#">READ MORE</a>
  </div>
  <div class="post-img" style="left:178px;top:346px;background:radial-gradient(circle at 45% 40%,#e0c1a6,#1f3a6b)" role="img" aria-label="Smiling man holding a bank card"></div>
  <div class="post" style="left:356px;top:351px">
    <h3>Pellentesque faucibus Ut accumsan ultricies elit Maecenas at justo</h3>
    <p>Aaculis ipsum dui aliquet felis at cursus magna nisl nec elit Praesent elementum elit at tellus nec ultricies sit amet porttitor mattis enim</p>
    <a href="#">READ MORE</a>
  </div>
  <div class="ad" style="top:87px;height:198px;background:linear-gradient(180deg,#2a1f3d,#1a1628)" role="img" aria-label="Advertisement banner for mortgage banking ads"></div>
  <div class="ad" style="top:301px;height:239px;background:linear-gradient(180deg,#d9e6f2 0%,#b7a07e 55%,#1f4f8f 78%,#1f4f8f 100%)" role="img" aria-label="Advertisement for a mortgage lender showing a couple in front of a house"></div>
</section>

<footer class="footer">
  <ul><li>Refinance</li><li>Buy a House</li><li>Loan Options</li><li>Mortgage Rates</li><li>About</li><li>Loan Calculator</li></ul>
  <small>© 2018 Company Name. All right reserved. Term of Use</small>
  <div class="social" aria-label="Social links"><span></span><span></span><span></span><span></span></div>
</footer>

</body>
</html>
```